Personal Chef Business Card Design

My company, Simmerly, is a personal in-home chef service that caters to clients' needs, but I am not a caterer. The types of services that I provide range from : weekly menus for busy families, special menus for specific diets, custom menus, private parties, intimate dinners, and brunch parties. My cooking style is seasonal and simple with the option of a variety of cuisines. I like colorful and simple business cards. My business is just getting started as I will be the only employee for now. I would like to be able to use the design on the card for my logo also. I don't know if logo design is a different service altogether.

If you can convince me to go with double-sided, then so be it, but until then, I'll stick with singe-sided.

Target Market(s)

busy families, health conscious, private parties, brunch parties, dinner parties

Industry/Entity Type

Chef

Contact Information for Business Card

Ross Tamblyn
rosstamblyn@mailvora.com
434-817-2290
Simmerly Personal Chef Service
Serving the DC/VA/MD area

Font styles to use
Serif
Sans Serif
Decorative
Script
Other font styles liked:
• Anything

Requirements
Must have
• I will be using the illustration as my logo so that I can use it for promotional merchandise.

```html
<!DOCTYPE html>
<html lang="en">
<head>
<meta charset="utf-8">
<title>Simmerly Personal Chef Service – Business Card</title>
<link rel="stylesheet" href="https://fonts.googleapis.com/css2?family=Amatic+SC:wght@400;700&family=Nunito:wght@400;600&display=swap">
<style>
  :root {
    --backdrop: #ecebe8;
    --card: #ffffff;
    --lime: #d6e15a;
    --lime-text: #c5d23c;
    --ink: #222222;
    --shadow: rgba(0, 0, 0, 0.12);
  }
  * { box-sizing: border-box; margin: 0; padding: 0; }
  html, body {
    width: 1200px;
    height: 1200px;
    overflow: hidden;
    background: var(--backdrop);
  }
  .canvas {
    width: 1200px;
    height: 1200px;
    display: flex;
    flex-direction: column;
    align-items: center;
    justify-content: center;
    gap: 70px;
  }
  .card {
    width: 700px;
    height: 400px;
    background: var(--card);
    box-shadow: 0 6px 18px var(--shadow);
    position: relative;
  }
  .brand {
    display: flex;
    align-items: center;
    gap: 20px;
  }
  .brand-dot {
    border-radius: 50%;
    background: var(--lime);
    flex: none;
  }
  .brand-name {
    font-family: "Nunito", sans-serif;
    font-weight: 600;
    color: var(--lime-text);
    line-height: 1.2;
    white-space: nowrap;
  }

  /* Reverse: services */
  .card--services {
    display: flex;
    flex-direction: column;
    align-items: center;
    justify-content: center;
    gap: 40px;
  }
  .card--services .brand-dot { width: 160px; height: 160px; }
  .card--services .brand-name { font-size: 26px; }
  .services {
    font-family: "Amatic SC", sans-serif;
    font-weight: 400;
    font-size: 32px;
    text-transform: uppercase;
    letter-spacing: 1px;
    color: var(--ink);
    text-align: center;
    line-height: 1.15;
  }
  .services .sep { margin: 0 10px; }

  /* Front: contact */
  .card--contact {
    display: flex;
    align-items: center;
    padding: 0 40px 0 50px;
    gap: 40px;
  }
  .card--contact .brand {
    flex-direction: column;
    gap: 16px;
    width: 250px;
    flex: none;
  }
  .card--contact .brand-dot { width: 220px; height: 220px; }
  .card--contact .brand-name { font-size: 17px; text-align: center; }
  .contact { padding-top: 10px; }
  .contact-name {
    font-family: "Amatic SC", sans-serif;
    font-weight: 400;
    font-size: 46px;
    text-transform: uppercase;
    letter-spacing: 4px;
    color: var(--lime-text);
    line-height: 1;
    margin-bottom: 22px;
    white-space: nowrap;
  }
  .contact-line {
    font-family: "Nunito", sans-serif;
    font-size: 19px;
    color: var(--ink);
    line-height: 1.45;
    white-space: nowrap;
  }
</style>
</head>
<body>
  <main class="canvas">
    <section class="card card--services" aria-label="Card reverse">
      <div class="brand">
        <span class="brand-dot"></span>
        <span class="brand-name">Simmerly<br>Personal Chef Service</span>
      </div>
      <p class="services">
        Private Parties<span class="sep">•</span>Intimate Dinners<br>
        Brunch Gatherings<span class="sep">•</span>Meal Planning
      </p>
    </section>

    <section class="card card--contact" aria-label="Card front">
      <div class="brand">
        <span class="brand-dot"></span>
        <span class="brand-name">Simmerly Personal Chef Service</span>
      </div>
      <div class="contact">
        <h1 class="contact-name">Dana Whitcombe</h1>
        <p class="contact-line">434-817-2290</p>
        <p class="contact-line">danawhitcombe@mailvora.com</p>
        <p class="contact-line">Serving the DC Metro area</p>
      </div>
    </section>
  </main>
</body>
</html>
```